Professional and Modern Company Letterhead for Fintech Startup

Brisk lending is a fintech startup that provides home financing.

Our company requires letterhead in Microsoft word format. Colors must come from our ADA compliant doc.

Company logo, equal housing opportunity logo, and legal language must be included somewhere on the document.

We'd love an option that maximizes space on the page for text vs have design take up the entire thing.

Target Market(s)

Partners, clients, and employees

Industry/Entity Type

Finance

Font styles to use
Sans Serif

Requirements
Must have
• Must use company colors that are ADA compliant (see attachment). Must include logo in a prominent position. Must include equal housing opportunity logo and legal info at the bottom:

©Brisk Lending LLC. NMLS #5093374 | 4716 Harlow Avenue #204, Boulder, CO 80305 | Not available in all states | 800.437.5068 | help@brisklending-example.com
Nice to have
• Something modern and clean.

```html
<!DOCTYPE html>
<html lang="en">
<head>
<meta charset="utf-8">
<title>Brisk Lending Letterhead</title>
<link href="https://fonts.googleapis.com/css2?family=Arimo:wght@400;700&family=Mrs+Saint+Delafield&display=swap" rel="stylesheet">
<style>
  :root {
    --navy: #0b2643;
    --orange: #e5854a;
    --ink: #111111;
    --paper: #ffffff;
  }
  html, body {
    margin: 0;
    padding: 0;
    width: 927px;
    height: 1200px;
    overflow: hidden;
    background: var(--paper);
  }
  .letterhead {
    position: relative;
    width: 927px;
    height: 1200px;
    font-family: "Arimo", Arial, sans-serif;
    color: var(--ink);
  }
  .header-shape {
    position: absolute;
    left: 0;
    top: 0;
  }
  .brand-name {
    position: absolute;
    left: 36px;
    top: 42px;
    margin: 0;
    font-size: 42px;
    font-weight: 700;
    color: var(--paper);
    line-height: 1;
  }
  .tagline {
    position: absolute;
    right: 34px;
    top: 35px;
    margin: 0;
    font-size: 25px;
    font-weight: 700;
    letter-spacing: 1.6px;
    color: var(--orange);
  }
  .date {
    position: absolute;
    right: 48px;
    top: 151px;
    font-size: 16.5px;
  }
  .salutation {
    position: absolute;
    left: 115px;
    top: 220px;
    margin: 0;
    font-size: 17px;
  }
  .closing {
    position: absolute;
    left: 129px;
    top: 871px;
    font-size: 17px;
  }
  .signature {
    position: absolute;
    left: 126px;
    top: 900px;
    font-family: "Mrs Saint Delafield", cursive;
    font-size: 38px;
    letter-spacing: 9px;
    line-height: 1;
  }
  .signer {
    position: absolute;
    left: 129px;
    top: 957px;
    font-size: 17px;
  }
  .eho-badge {
    position: absolute;
    left: 42px;
    top: 1107px;
    width: 70px;
    height: 68px;
    border: 3px solid var(--ink);
    box-sizing: border-box;
  }
  .legal-band {
    position: absolute;
    left: 126px;
    top: 1090px;
    width: 764px;
    height: 88px;
    background: var(--navy);
    color: var(--orange);
    font-weight: 700;
    font-size: 15px;
    letter-spacing: 0.9px;
    text-align: center;
    display: flex;
    flex-direction: column;
    justify-content: center;
    gap: 4px;
  }
  .legal-band p { margin: 0; line-height: 18px; }
</style>
</head>
<body>
<div class="letterhead">
  <svg class="header-shape" width="927" height="260" viewBox="0 0 927 260" aria-hidden="true">
    <polygon points="22,11 906,11 906,85 349,85 22,248" fill="var(--navy)"/>
  </svg>

  <p class="brand-name">Brisk lending</p>

  <p class="tagline">Finance your home—the Brisk way.</p>

  <div class="date">Date: ##/##/####</div>

  <p class="salutation">To Whom This May Concern,</p>

  <div class="closing">Kind Regards,</div>
  <div class="signature">Staff Name</div>
  <div class="signer">Brisk Lending Staff</div>

  <div class="eho-badge" role="img" aria-label="Equal housing opportunity badge"></div>

  <footer class="legal-band">
    <p>©Brisk Lending LLC. NMLS #5093374 | 4716 Harlow Avenue #204, Boulder, CO 80305</p>
    <p>| Not available in all states |</p>
    <p>800.437.5068 | help@brisklending-example.com</p>
  </footer>
</div>
</body>
</html>
```